Magnet for side of van (Al or eps)

I have some old files on my computer, so I created an image to make this project easier. The company making the magnet is requesting vector files. Specifically Al or eps. The size of the magnet that will fit on the van is approx. 30" x 10". I would like the design to work on any size magnet that can be ordered, but definitely close to the size provided. The magnet will be placed on a dark grey van so the background needs to be light color, white is fine. Not sure if they are cutting this out with a cutter, so if the graphics have to be lighter, then so be it. I'll update designers with that status soon. If you can keep the shades and the colors that would be nice, making solid colors would be fine too. Any new graphics would be nice, but not necessary. Fonts of the phone number and website can be changed if needed. Location of logo, name, number, or website address can be moved around if necessary. If you can add "Quality You Deserve", that would be nice, but not necessary. Letters BRM IS NOT necessary for this project. Just sending you the al and eps file if it helps for creation. I would like the colors be the same or close. Any questions, feel free to ask, if you need more ideas or details.
Industry/Entity Type
Computer
Requirements
Must have
- Company logo and name, telephone number and website.

```html
<!DOCTYPE html>
<html lang="en">
<head>
<meta charset="utf-8">
<title>Bright River Glass – Van Magnet</title>
<link rel="stylesheet" href="https://fonts.googleapis.com/css2?family=Montserrat:wght@700&family=Great+Vibes&display=swap">
<style>
  :root {
    --backdrop: #2a2a2a;
    --magnet-top: #ffffff;
    --magnet-bottom: #e6e6e6;
    --brand-blue: #1f5fae;
    --mark-blue: #1f78c8;
    --contact-blue: #1a4a94;
    --script-ink: #333333;
  }
  * { margin: 0; padding: 0; box-sizing: border-box; }
  html, body {
    width: 1200px;
    height: 1000px;
    overflow: hidden;
    background: var(--backdrop);
  }
  .magnet {
    position: absolute;
    left: 60px;
    top: 320px;
    width: 1080px;
    height: 360px;
    background: linear-gradient(180deg, var(--magnet-top) 0%, var(--magnet-top) 45%, var(--magnet-bottom) 100%);
  }
  .brand-square {
    position: absolute;
    left: 70px;
    top: 95px;
    width: 170px;
    height: 170px;
    background: var(--mark-blue);
  }
  .brand-name {
    position: absolute;
    left: 330px;
    top: 52px;
    width: 730px;
    text-align: center;
    font-family: "Montserrat", sans-serif;
    font-weight: 700;
    font-size: 58px;
    line-height: 1;
    color: var(--brand-blue);
    white-space: nowrap;
  }
  .tagline {
    position: absolute;
    left: 330px;
    top: 172px;
    width: 730px;
    text-align: center;
    font-family: "Great Vibes", cursive;
    font-size: 66px;
    line-height: 1;
    color: var(--script-ink);
  }
  .contact {
    position: absolute;
    left: 330px;
    top: 284px;
    width: 730px;
    display: flex;
    justify-content: center;
    gap: 30px;
    font-family: "Montserrat", sans-serif;
    font-weight: 700;
    font-size: 31px;
    line-height: 40px;
    color: var(--contact-blue);
  }
  .contact-item {
    display: flex;
    align-items: center;
    gap: 10px;
  }
  .contact-icon {
    width: 36px;
    height: 36px;
    flex: none;
  }
</style>
</head>
<body>
  <div class="magnet">
    <div class="brand-square"></div>
    <div class="brand-name">Bright River Glass</div>
    <div class="tagline">Quality you deserve!</div>
    <div class="contact">
      <div class="contact-item">
        <svg class="contact-icon" viewBox="0 0 36 36" aria-hidden="true">
          <circle cx="18" cy="18" r="18" fill="var(--contact-blue)"/>
          <path d="M12.5 9.5c1-.6 2-.3 2.5.6l1.6 3c.4.8.2 1.6-.4 2.1l-1.2 1c.9 2 2.5 3.6 4.5 4.6l1-1.2c.5-.6 1.4-.8 2.1-.4l3 1.6c.9.5 1.2 1.5.6 2.5l-1 1.6c-.7 1.1-2 1.6-3.2 1.2-5.4-1.7-9.6-5.9-11.3-11.3-.4-1.2.1-2.5 1.2-3.2z" fill="#ffffff"/>
        </svg>
        <span class="contact-phone">(555)010-4477</span>
      </div>
      <div class="contact-item">
        <svg class="contact-icon" viewBox="0 0 36 36" aria-hidden="true" fill="none" stroke="var(--contact-blue)" stroke-width="2">
          <circle cx="18" cy="18" r="16"/>
          <ellipse cx="18" cy="18" rx="7" ry="16"/>
          <line x1="18" y1="2" x2="18" y2="34"/>
          <line x1="2" y1="18" x2="34" y2="18"/>
          <path d="M5 10h26M5 26h26"/>
        </svg>
        <span class="contact-web">www.brmglass.com</span>
      </div>
    </div>
  </div>
</body>
</html>
```